Bright Haven Estate Sales web design

We are looking to launch an Estate Sales Website for Nashville, TN. The name of our Business is Bright Haven Estate Sales. We would like to give you a blank slate so that you can showcase your design skills for us. The few things we are looking for are a nice header graphic of a house or a stock image of an estate sale. Near the header graphic we would like a quick inquiry form. If not on the right side of the header maybe midway down the site. We potentially want to see what purple and Gold look like on the site however this is not a must. We have over 20 years of industry related experience.

1. Buttons at top of the website will be.
a. Services
b. Upcoming Sales
c. About Us
d. FAQs
e. Resources

Services we offer:
1. Estate Sales
2. Cleanouts
3. Appraisals

Sites We like:
https://www.corvellestatesales.example/

We don't have a logo yet so if you have ideas please share them with us. Below are 2 ideas however if you have your own thoughts please ignore.

1. Oval ornate frame, gold and black, with BHES in the middle, deep purple. Think of catering to high class people..font should be fancy as opposed to simple.

2. Another option, Bright Haven in bold fancy script, same colors, with Estate Sales below, small different font, black.

```html
<!DOCTYPE html>
<html lang="en">
<head>
<meta charset="utf-8">
<title>Bright Haven Estate Sales</title>
<link href="https://fonts.googleapis.com/css2?family=Playfair+Display:wght@500;600;700&family=Poppins:wght@400;500;600&display=swap" rel="stylesheet">
<style>
:root{
  --purple:#8c0c8e;
  --purple-deep:#6a1aa8;
  --gold:#ffd800;
  --cream:#fffbea;
  --ink:#1c1c1c;
  --muted:#6d6d6d;
  --stage:#2e2e2e;
  --white:#ffffff;
}
*{box-sizing:border-box;margin:0;padding:0}
html,body{width:1200px;height:4040px;overflow:hidden}
body{position:relative;background:var(--stage);font-family:'Poppins',sans-serif;color:var(--ink)}
.page{position:absolute;top:250px;left:0;width:1200px;height:3540px;overflow:hidden;background:var(--white)}
.btn{display:inline-block;background:var(--gold);color:var(--ink);font-size:10px;font-weight:600;padding:8px 22px;border-radius:3px}
.section-title{font-family:'Playfair Display',serif;font-weight:600;font-size:26px;text-align:center}
.section-sub{font-size:11px;color:var(--muted);text-align:center;line-height:22px}

/* hero */
.hero{position:relative;height:675px;overflow:hidden}
.brand{position:absolute;left:62px;top:42px;font-family:'Playfair Display',serif;font-weight:700;color:var(--purple);font-size:17px;line-height:14px}
.brand small{display:block;font-size:7px;letter-spacing:2px;margin-top:4px}
.nav{position:absolute;left:230px;top:54px;display:flex;gap:26px;font-size:11px;color:#444}
.nav .active{color:var(--ink);font-weight:600}
.hero h1{position:absolute;left:62px;top:170px;width:580px;font-family:'Playfair Display',serif;font-weight:600;font-size:52px;line-height:60px}
.hero .lead{position:absolute;left:62px;top:375px;width:540px;font-size:14px;line-height:22px;color:#333}
.hero .btn{position:absolute;left:62px;top:448px}
.arrows{position:absolute;left:62px;top:540px;display:flex;gap:56px}
.hero-photo{position:absolute;left:686px;top:0;width:514px;height:675px;background:linear-gradient(160deg,#d7dde4 0%,#b3a597 40%,#7b6550 70%,#4a5a66 100%)}
.outline-word{position:absolute;left:700px;width:500px;overflow:hidden;font-family:'Playfair Display',serif;font-size:112px;line-height:112px;color:transparent;-webkit-text-stroke:1.5px var(--white);white-space:nowrap}
.outline-word.second{left:780px;width:420px}
.stats{position:absolute;right:0;bottom:0;width:200px;height:246px;background:var(--purple);color:var(--white);padding:32px 0 0 60px}
.stats b{font-family:'Playfair Display',serif;font-size:20px;font-weight:500}
.stats p{font-size:13px;line-height:20px;margin:6px 0 28px}

/* services */
.services{height:414px;background:var(--cream);padding-top:64px}
.cards{display:flex;gap:20px;justify-content:center;margin-top:52px}
.card{width:302px;height:124px;background:var(--white);border-radius:6px;box-shadow:0 6px 18px rgba(0,0,0,.08);display:flex;gap:16px;padding:28px 18px}
.card .ico{flex:none;width:52px;height:52px;border-radius:50%;background:var(--gold);display:flex;align-items:center;justify-content:center}
.card h3{font-family:'Playfair Display',serif;font-size:14px;font-weight:600;margin-bottom:8px}
.card p{font-size:9px;line-height:15px;color:var(--muted)}

/* upcoming */
.upcoming{height:748px;background:linear-gradient(135deg,#9a1eaa 0%,#7b23c4 45%,#a012a5 100%);color:var(--white);padding-top:80px}
.upcoming .section-sub{color:#f2dff6}
.listings{display:flex;gap:20px;justify-content:center;margin-top:50px;align-items:flex-start}
.listing{width:283px}
.listing.raised{margin-top:-24px}
.listing .shot{height:323px;border-radius:8px}
.listing.raised .shot{height:310px}
.meta{display:flex;justify-content:space-between;padding:22px 14px 0}
.meta .loc{display:flex;gap:10px;font-size:13px;font-weight:500}
.meta .loc span{display:block;font-size:9px;font-weight:400;color:#efd8f5}
.stars{color:var(--gold);font-size:12px;letter-spacing:2px;padding-top:8px}
.upcoming .center{text-align:center;margin-top:34px}

/* inquiry */
.inquiry{height:290px;padding-top:100px}
.inquiry .section-title{font-size:25px}
.form{display:flex;gap:6px;justify-content:center;margin-top:24px}
.field{width:160px;height:30px;border:1px solid #e2e2e2;border-radius:3px;font-size:9px;color:#888;display:flex;align-items:center;gap:6px;padding-left:12px}
.form .btn{height:30px;width:112px;text-align:center}

/* about */
.about{position:relative;height:590px;overflow:hidden}
.about .ring{position:absolute;left:152px;top:10px;width:430px;height:430px;border-radius:50%;border:1px solid #e6d6ea}
.about .glow{position:absolute;left:300px;top:20px;width:240px;height:240px;border-radius:50%;background:#fbeefd}
.about .shot{position:absolute;left:212px;top:86px;width:358px;height:302px;background:linear-gradient(180deg,#cfe6f2 0%,#e9e3cf 45%,#5ec0d6 75%,#2f93b8 100%)}
.trust{position:absolute;left:380px;top:368px;width:208px;height:106px;background:var(--white);box-shadow:0 6px 18px rgba(0,0,0,.1);border-radius:4px;padding:16px 22px}
.trust h4{font-family:'Playfair Display',serif;font-size:10px;font-weight:500;color:#666;margin-bottom:10px}
.avatars{display:flex}
.avatars i{width:34px;height:34px;border-radius:50%;border:2px solid var(--white);margin-right:-8px;background:#c9a58a}
.avatars i:nth-child(2){background:#8a6a57}.avatars i:nth-child(3){background:#d98b5a}.avatars i:nth-child(4){background:#6b5046}.avatars i:nth-child(5){background:#b89a86}
.mark{position:absolute;color:var(--purple);font-size:16px}
.dot{position:absolute;width:14px;height:14px;border:1.5px solid var(--purple);border-radius:50%}
.about .copy{position:absolute;left:656px;top:190px;width:370px}
.about h2{font-family:'Playfair Display',serif;font-size:24px;font-weight:600;color:var(--purple);margin-bottom:18px}
.about p{font-size:11px;line-height:22px;color:var(--muted);margin-bottom:16px}

/* faq */
.faq{height:535px;background:linear-gradient(180deg,#fff6cc 0%,#fff0b0 50%,#fff4c4 100%);padding-top:70px}
.faq .section-sub{width:520px;margin:14px auto 0}
.faq-list{width:880px;margin:24px auto 0;display:flex;flex-direction:column;gap:12px}
.faq-item{height:41px;background:var(--gold);display:flex;justify-content:space-between;align-items:center;padding:0 32px;font-size:11px;font-weight:500}
.faq-item span{color:#c9a400;font-size:14px}
.contact-btn{display:block;width:160px;margin:18px auto 0;background:var(--purple);color:var(--white);font-size:9px;font-weight:600;text-align:center;padding:14px 0}

/* footer */
.footer{position:relative;height:288px;background:var(--gold);padding:54px 0 0 156px;display:flex;font-size:9px}
.footer .brand{position:static;margin-bottom:20px}
.col{width:158px}
.col.first{width:262px}
.col h5{font-family:'Playfair Display',serif;font-size:12px;font-weight:600;margin-bottom:18px}
.col a{display:block;color:#8a6a2e;margin-bottom:14px;text-decoration:none}
.col p{color:#6d5a25;line-height:16px}
.socials{display:flex;gap:10px;margin-top:18px}
.socials i{width:18px;height:18px;border-radius:50%;background:#ffc7c0}
.contact-col{width:200px}
.contact-col p{margin-bottom:14px;color:var(--ink)}
.copyright{position:absolute;left:0;right:0;bottom:24px;text-align:center;color:#a07a2a;font-size:9px}
</style>
</head>
<body>
<main class="page">

  <section class="hero">
    <div class="brand">Bright Haven<small>ESTATE SALES</small></div>
    <nav class="nav"><span class="active">Home</span><span>Services</span><span>Upcoming Sales</span><span>About Us</span><span>FAQs</span><span>Resources</span></nav>
    <h1>Elevate Your Estate Experience with Bright Haven Estate Sales.</h1>
    <p class="lead">We open the doors to a world of possibilities, ensuring every item finds its perfect home. Backed by over 20 years of industry expertise...</p>
    <span class="btn">Learn More ›</span>
    <div class="arrows">
      <svg width="16" height="26" viewBox="0 0 16 26"><path d="M14 2 3 13l11 11" fill="none" stroke="#8c0c8e" stroke-width="2"/></svg>
      <svg width="16" height="26" viewBox="0 0 16 26"><path d="M2 2l11 11L2 24" fill="none" stroke="#1c1c1c" stroke-width="2"/></svg>
    </div>
    <div class="hero-photo" role="img" aria-label="Photo of a modern luxury villa with curving white balconies at dusk"></div>
    <div class="outline-word" style="top:16px">Luxury</div>
    <div class="outline-word second" style="top:128px">Estate</div>
    <div class="stats">
      <b>20+</b><p>Years of<br>Experience</p>
      <b>700+</b><p>Satisfied<br>Clients</p>
    </div>
  </section>

  <section class="services">
    <h2 class="section-title">Our Services</h2>
    <p class="section-sub" style="margin-top:18px">We open the doors to a world of possibilities, ensuring every item finds its perfect home.</p>
    <div class="cards">
      <div class="card">
        <div class="ico"><svg width="24" height="24" viewBox="0 0 24 24"><path d="M3 11 12 4l9 7v9H3z" fill="#1c1c1c"/></svg></div>
        <div><h3>Estate Sales</h3><p>Explore our meticulously curated estate sales, featuring unique finds and treasures.</p></div>
      </div>
      <div class="card">
        <div class="ico"><svg width="24" height="24" viewBox="0 0 24 24"><path d="M5 9h14l-2 12H7z M9 9V5h6v4" fill="#1c1c1c"/></svg></div>
        <div><h3>Cleanouts</h3><p>Seamless cleanouts for a hassle-free transition. Trust us to handle every detail with care.</p></div>
      </div>
      <div class="card">
        <div class="ico"><svg width="24" height="24" viewBox="0 0 24 24"><rect x="6" y="3" width="12" height="18" rx="1" fill="#1c1c1c"/><path d="M9 8h6M9 12h6M9 16h6" stroke="#ffd800" stroke-width="1.5"/></svg></div>
        <div><h3>Appraisals</h3><p>Accurate and detailed appraisals for your valuable possessions. Uncover the true worth with Bright Haven.</p></div>
      </div>
    </div>
  </section>

  <section class="upcoming">
    <h2 class="section-title">Discover our Upcoming Sales</h2>
    <p class="section-sub" style="margin-top:12px">With a legacy of over 20 years in the industry, our team is dedicated to professionalism,<br>reliability, and the utmost care.</p>
    <div class="listings">
      <div class="listing">
        <div class="shot" role="img" aria-label="Photo of a white modern house with warm lit windows" style="background:linear-gradient(160deg,#b9d3ea 0%,#f0f0f0 45%,#e2743a 70%,#3d3f48 100%)"></div>
        <div class="meta"><div class="loc"><svg width="12" height="16" viewBox="0 0 12 16"><path d="M6 0a6 6 0 0 1 6 6c0 4-6 10-6 10S0 10 0 6a6 6 0 0 1 6-6z" fill="#ffd800"/><circle cx="6" cy="6" r="2" fill="#8c0c8e"/></svg><div>Location 01<span>5d - 4n</span></div></div><div class="stars">★★★★★</div></div>
      </div>
      <div class="listing raised">
        <div class="shot" role="img" aria-label="Photo of a classic mansion lit up at night" style="background:linear-gradient(180deg,#1a1a24 0%,#6e5a2a 40%,#d5b04a 65%,#2a2a1e 100%)"></div>
        <div class="meta"><div class="loc"><svg width="12" height="16" viewBox="0 0 12 16"><path d="M6 0a6 6 0 0 1 6 6c0 4-6 10-6 10S0 10 0 6a6 6 0 0 1 6-6z" fill="#ffd800"/><circle cx="6" cy="6" r="2" fill="#8c0c8e"/></svg><div>Location 02<span>5d - 4n</span></div></div><div class="stars">★★★★★</div></div>
      </div>
      <div class="listing">
        <div class="shot" role="img" aria-label="Photo of a modern multi-storey glass residence" style="background:linear-gradient(180deg,#e9eef0 0%,#cfd6d6 50%,#7f8a80 80%,#4f5a52 100%)"></div>
        <div class="meta"><div class="loc"><svg width="12" height="16" viewBox="0 0 12 16"><path d="M6 0a6 6 0 0 1 6 6c0 4-6 10-6 10S0 10 0 6a6 6 0 0 1 6-6z" fill="#ffd800"/><circle cx="6" cy="6" r="2" fill="#8c0c8e"/></svg><div>Location 03<span>5d - 4n</span></div></div><div class="stars">★★★★★</div></div>
      </div>
    </div>
    <div class="center"><span class="btn">View More ›</span></div>
  </section>

  <section class="inquiry">
    <h2 class="section-title">Bright Haven Estate Sales - Where Every Possession Finds a Perfect Home.</h2>
    <p class="section-sub" style="margin-top:10px">We are your partners in the journey of transitioning possessions.</p>
    <div class="form">
      <div class="field">👤 Username</div>
      <div class="field">✉ Email</div>
      <div class="field">✆ Phone</div>
      <div class="field">✎ Type Your Message</div>
      <span class="btn">Submit ›</span>
    </div>
  </section>

  <section class="about">
    <div class="glow"></div>
    <div class="ring"></div>
    <div class="shot" role="img" aria-label="Photo of a white colonnaded estate with palm trees and a pool"></div>
    <div class="trust">
      <h4>People Who Trusted Us!</h4>
      <div class="avatars" role="img" aria-label="Small portrait photos of satisfied clients"><i></i><i></i><i></i><i></i><i></i></div>
    </div>
    <span class="dot" style="left:525px;top:0"></span>
    <span class="dot" style="left:132px;top:368px"></span>
    <span class="mark" style="left:160px;top:180px">+</span>
    <span class="mark" style="left:585px;top:160px">+</span>
    <span class="mark" style="left:526px;top:500px">+</span>
    <div class="copy">
      <h2>About Bright Haven Estate Sales</h2>
      <p>At Bright Haven Estate Sales, we are more than just a service; we are your partners in the journey of transitioning possessions. With a legacy of over 20 years in the industry, our team is dedicated to professionalism, reliability, and the utmost care.</p>
      <span class="btn">Learn More ›</span>
    </div>
  </section>

  <section class="faq">
    <h2 class="section-title">Frequently Asked Questions.</h2>
    <p class="section-sub">Answers to common questions about our services, safety measures, and project execution. Get the information you need quickly and efficiently.</p>
    <div class="faq-list">
      <div class="faq-item">Lorem ipsum dolor sit amet, consectetur adipiscing elit?<span>+</span></div>
      <div class="faq-item">Lorem ipsum dolor sit amet, consectetur adipiscing elit?<span>+</span></div>
      <div class="faq-item">Lorem ipsum dolor sit amet, consectetur adipiscing elit?<span>+</span></div>
      <div class="faq-item">Lorem ipsum dolor sit amet, consectetur adipiscing elit?<span>+</span></div>
    </div>
    <span class="contact-btn">CONTACT US ›</span>
  </section>

  <footer class="footer">
    <div class="col first">
      <div class="brand">Bright Haven<small>ESTATE SALES</small></div>
      <p>Elevate Your Estate Experience<br>with Bright Haven Estate Sales.</p>
      <div class="socials"><i></i><i></i><i></i><i></i></div>
    </div>
    <div class="col"><h5>Services</h5><a>Estate Sales</a><a>Cleanouts</a><a>Appraisals</a></div>
    <div class="col"><h5>Company</h5><a>Services</a><a>Upcoming Sales</a><a>FAQs</a><a>About Us</a></div>
    <div class="col"><h5>Company</h5><a>Legal</a><a>Terms</a><a>Privacy Policy</a></div>
    <div class="contact-col col"><h5>Contact</h5><p>Call : +1 615 555 0142</p><p>Email : contact@brighthaven.example</p><p>Address : Street 12, Nashville, TN</p></div>
    <div class="copyright">Copyright© 2024 Bright Haven Estate Sales. All right reserved.</div>
  </footer>

</main>
</body>
</html>
```